Everything fresh, everything new

When I take over the practice, I would like to breathe new life into the practice. I want a business card design that catches the eye and brings a breath of fresh air

```html
<!DOCTYPE html>
<html lang="de">
<head>
<meta charset="utf-8">
<title>Vitalwerk – Visitenkarte</title>
<link rel="stylesheet" href="https://fonts.googleapis.com/css2?family=Montserrat:wght@500;700&family=Arimo:wght@400&display=swap">
<style>
  :root {
    --backdrop: #d3d6d7;
    --paper: #f7f7f5;
    --ink: #1d1d1d;
    --ink-soft: #3a3a3a;
    --green: #5aa514;
    --green-pale: #c9e39a;
  }
  * { margin: 0; padding: 0; box-sizing: border-box; }
  html, body {
    width: 1200px;
    height: 829px;
    overflow: hidden;
    background: var(--backdrop);
  }
  .canvas {
    position: relative;
    width: 1200px;
    height: 829px;
    display: flex;
    align-items: center;
    justify-content: center;
    gap: 40px;
  }
  .card {
    position: relative;
    width: 540px;
    height: 310px;
    background: var(--paper);
    border-bottom: 4px solid var(--green);
    overflow: hidden;
  }

  /* Brand lockup */
  .brand {
    position: absolute;
    display: flex;
    align-items: center;
    gap: 8px;
    font-family: "Montserrat", sans-serif;
    font-weight: 500;
    color: var(--ink);
    white-space: nowrap;
  }
  .brand-dot {
    border-radius: 50%;
    background: var(--green);
  }
  .tagline {
    position: absolute;
    font-family: "Montserrat", sans-serif;
    font-weight: 500;
    color: var(--ink-soft);
    white-space: nowrap;
  }

  /* Front face */
  .front .brand {
    left: 48px;
    top: 34px;
    font-size: 24px;
  }
  .front .brand-dot { width: 12px; height: 12px; }
  .front .tagline {
    left: 49px;
    top: 67px;
    font-size: 9px;
  }
  .accent-bar {
    position: absolute;
    left: 0;
    top: 104px;
    width: 14px;
    height: 32px;
    background: var(--green);
  }
  .holder-name {
    position: absolute;
    left: 48px;
    top: 104px;
    font-family: "Montserrat", sans-serif;
    font-weight: 700;
    font-size: 19px;
    letter-spacing: 0.5px;
    color: var(--green);
    white-space: nowrap;
  }
  .holder-role {
    position: absolute;
    left: 48px;
    top: 128px;
    font-family: "Arimo", sans-serif;
    font-size: 13px;
    color: var(--ink-soft);
  }
  .contact-list {
    position: absolute;
    left: 48px;
    top: 160px;
    list-style: none;
    font-family: "Arimo", sans-serif;
    font-size: 13px;
    color: var(--ink);
  }
  .contact-list li {
    display: flex;
    align-items: center;
    gap: 7px;
    height: 21px;
    white-space: nowrap;
  }
  .contact-list svg {
    width: 11px;
    height: 11px;
    fill: var(--green);
    flex: none;
  }
  .decor-circle {
    position: absolute;
    right: 36px;
    top: 34px;
    width: 240px;
    height: 240px;
    border-radius: 50%;
    background: var(--green-pale);
    opacity: 0.55;
  }

  /* Back face */
  .back .brand {
    left: 50%;
    top: 118px;
    transform: translateX(-50%);
    font-size: 40px;
    gap: 12px;
  }
  .back .brand-dot { width: 20px; height: 20px; }
  .back .tagline {
    left: 0;
    right: 0;
    top: 176px;
    text-align: center;
    font-size: 12px;
  }
</style>
</head>
<body>
<main class="canvas">

  <section class="card front">
    <div class="brand"><span class="brand-name">Vitalwerk</span><span class="brand-dot"></span></div>
    <p class="tagline">Praxis für Physiotherapie</p>

    <span class="accent-bar"></span>
    <h1 class="holder-name">LENA HARTMANN</h1>
    <p class="holder-role">Owner/CEO</p>

    <ul class="contact-list">
      <li>
        <svg viewBox="0 0 16 16" aria-hidden="true"><path d="M3.5 1.5l2.5 0 1.2 3.2-1.6 1.2c.8 1.8 2.2 3.2 4 4l1.2-1.6 3.2 1.2v2.5c0 .8-.7 1.5-1.5 1.5C6.9 13.5 2 8.6 2 3c0-.8.7-1.5 1.5-1.5z"/></svg>
        555-210-48730
      </li>
      <li>
        <svg viewBox="0 0 16 16" aria-hidden="true"><path d="M4.5 1h7c.6 0 1 .4 1 1v12c0 .6-.4 1-1 1h-7c-.6 0-1-.4-1-1V2c0-.6.4-1 1-1zm.5 2v9h6V3H5zm3 10a.8.8 0 100 1.6.8.8 0 000-1.6z"/></svg>
        555-310-48731
      </li>
      <li>
        <svg viewBox="0 0 16 16" aria-hidden="true"><path d="M1 3h14v10H1V3zm1.6 1.2L8 8.3l5.4-4.1H2.6zM2 5.3V12h12V5.3L8 9.8 2 5.3z"/></svg>
        hallo@vitalwerk-praxis.de
      </li>
      <li>
        <svg viewBox="0 0 16 16" aria-hidden="true"><circle cx="8" cy="8" r="7"/></svg>
        www.vitalwerk-praxis.de
      </li>
    </ul>

    <div class="decor-circle" role="img" aria-label="Große dekorative Kreisform in hellem Grün"></div>
  </section>

  <section class="card back">
    <div class="brand"><span class="brand-name">Vitalwerk</span><span class="brand-dot"></span></div>
    <p class="tagline">Praxis für Physiotherapie</p>
  </section>

</main>
</body>
</html>
```